Talvane Salmon Labels

We need a graphic design label for a new product launch. Talvane is an 100% Australian family business specialised in making marinades made from natural and locally sourced fresh ingredients for fish and seafood. We make remarkable food for fine cooking prepared by hand at our kitchen in Condell Park, using the same ingredients and techniques you would use at home.

We are planning to launch three marinades for salmon.
The flavours are:

- Herb, Lemon & Cracked Black Pepper
- Ginger, Honey & Soy
- Coriander, Lemongrass, Shallot and Ginger

The marinades will be packed in a 300 grams clear pouch with spout and sold in the seafood section of a major retail supermarket.

Measurements of the pouch: 140 mm wide and 210 mm high but only 160 mm high from the spout downwards.

Label: For the label, It will be a 120mm wide X 120mm high If not slightly smaller. Please refer to File 2: to see the pouch.

The label will cover 75% of the front of the pouch and the marinade itself will be visible in the remaining 25 % of the pouch. The colours of the marinades are green for Herb, Lemon & Cracked Black Pepper and Coriander, Lemongrass, Shallot and Ginger; and dark brown for Ginger, Honey & Soy.

Our marinades do not contain additives. The marinades are Gluten free.

The label needs to visually communicate that the marinade is used for salmon.

Please choose a suitable typography for our name Talvane that communicates an artisan feel.

Please refer to File 1 as a guide to what we would like, but keep in mind we are very open to any ideas you may have.

Colours should reflect the nature of our business, as outlined above.
Updates

Hello Designers,

This is what the actual pouch looks like https://www.filecrate.example/sc/4kd82mz19qp0x/Tq73Lowm8_

We would like the label to be roughly 120mm X 120mm or within those parameters to fit the packaging.

Thank you!
- Miriam

Hey Designers,

we have been looking at your designs and while we have liked some elements of them we would like to see more creativity with the actual graphics and shapes of the labels, different colour contrast and more clever and quirky designs. We want to make fish fun and interesting to consumers, something rustic that catches the eye but at the same time is still sophisticated and upmarket. 

We would like to see the following on your packaging designs:

- Pastels colours (green, blue and yellow).
- The 'Talvane gourmet' font to be in bolder typography
- An ink looking stamp for 'gluten free, no additives'
- Something about the product being hand crafted
- Must include the following text: Marinades made from natural and locally sourced fresh ingredients for fish and seafood

here are some examples for you to be inspired by

Some font ideas ..

http://pinboardly.example/pin/501928374650192837/
http://pinboardly.example/pin/73019284756102938/
http://pinboardly.example/pin/618293047561829304/
http://pinboardly.example/pin/339201847562019384/
http://pinboardly.example/pin/447102938475610293/
http://pinboardly.example/pin/582019374651029384/

colours/images/graphics

http://pinboardly.example/pin/194820375619203847/
http://pinboardly.example/pin/730192846501928374/
http://pinboardly.example/pin/865019283746501927/
http://pinboardly.example/pin/412093847561029384/ (We like this concept) 

Good luck! 

 

Target Market(s)

Home cooks, young professionals, anyone with a healthy eating lifestyle.

Industry/Entity Type

Graphic Design

Requirements
Must have
• The label needs to visually communicate that the marinade is used for salmon.
- Include "Gluten Free" and "No Additives" on the label
- Outline the freshness of the ingredients used in the marinade eg. Coriander, Lemongrass, Shallot and Ginger to be included on the label.
- Bright and eye catching colours (food friendly colours).
Nice to have
• - Open to pastel colours
- Vector drawings
Should not have
• - dull colours

```html
<!DOCTYPE html>
<html lang="en">
<head>
<meta charset="utf-8">
<title>Talvane Salmon Marinade Label</title>
<link rel="stylesheet" href="https://fonts.googleapis.com/css2?family=Cinzel:wght@400&family=Tinos:ital,wght@0,400;0,700;1,400&display=swap">
<style>
  :root {
    --page: #ffffff;
    --panel: #7a9680;
    --ink: #111111;
    --cream: #ffffff;
  }
  html, body {
    margin: 0;
    padding: 0;
    overflow: hidden;
    background: var(--page);
  }
  .canvas {
    position: relative;
    width: 927px;
    height: 1200px;
    background: var(--page);
    overflow: hidden;
  }
  .label-frame {
    position: absolute;
    left: 0;
    top: 0;
  }
  .label-text {
    position: absolute;
    left: 216px;
    width: 496px;
    text-align: center;
    margin: 0;
  }
  .brand-name {
    top: 318px;
    font-family: "Cinzel", serif;
    font-weight: 400;
    font-size: 58px;
    letter-spacing: 2px;
    line-height: 1;
    color: var(--cream);
  }
  .origin {
    top: 392px;
    font-family: "Tinos", serif;
    font-size: 20px;
    letter-spacing: 1px;
    line-height: 1;
    color: var(--cream);
  }
  .product-type {
    top: 428px;
    font-family: "Tinos", serif;
    font-size: 28px;
    letter-spacing: 1.5px;
    line-height: 1;
    color: var(--ink);
  }
  .flavour {
    top: 527px;
    font-family: "Tinos", serif;
    font-weight: 700;
    font-size: 26px;
    line-height: 31px;
    letter-spacing: 0.5px;
    color: var(--ink);
  }
  .salmon-art {
    position: absolute;
    left: 288px;
    top: 628px;
    width: 338px;
    height: 122px;
    background: var(--ink);
    border-radius: 40% 55% 50% 30% / 50% 50% 50% 50%;
  }
  .claims {
    top: 764px;
    font-family: "Tinos", serif;
    font-weight: 700;
    font-size: 13px;
    letter-spacing: 1.5px;
    line-height: 1;
    color: var(--ink);
  }
  .tagline {
    top: 783px;
    font-family: "Tinos", serif;
    font-style: italic;
    font-size: 11.5px;
    line-height: 1;
    color: var(--cream);
  }
</style>
</head>
<body>
  <main class="canvas">
    <svg class="label-frame" width="927" height="1200" viewBox="0 0 927 1200" aria-hidden="true">
      <g fill="none" stroke="var(--ink)">
        <rect x="190" y="283" width="547" height="549" rx="40" stroke-width="2"/>
        <rect x="194" y="287" width="539" height="541" rx="38" stroke-width="1.5"/>
        <rect x="198" y="291" width="531" height="533" rx="36" stroke-width="2"/>
        <rect x="202" y="295" width="523" height="525" rx="34" stroke-width="1.5"/>
        <rect x="206" y="299" width="515" height="517" rx="32" stroke-width="2.5"/>
      </g>
      <rect x="211" y="304" width="505" height="507" rx="28" fill="var(--ink)"/>
      <rect x="216" y="308" width="496" height="498" rx="24" fill="var(--panel)" stroke="var(--cream)" stroke-width="3"/>
    </svg>

    <h1 class="label-text brand-name">TALVANE</h1>
    <p class="label-text origin">100% AUSTRALIAN</p>
    <p class="label-text product-type">SALMON MARINADE</p>
    <p class="label-text flavour">CORIANDER, LEMONGRASS,<br>SHALLOT AND GINGER</p>

    <div class="salmon-art" role="img" aria-label="Black silhouette illustration of a salmon swimming left to right"></div>

    <p class="label-text claims">GLUTEN FREE &middot; NO ADDITIVES</p>
    <p class="label-text tagline">Marinades made from natural and locally sourced fresh ingredients for fish and seafood</p>
  </main>
</body>
</html>
```